Aircraft Spares Supplier
Stationary/Business Cards
Project: Aircraft Spares Supplier
Aircraft Spares Supplier  - Aviation
Creative Brief
Use standard fonts
I am flexible on the font
Rowan Pettibone
Managing Director
PO Box 71829 Marrow Bay Freezone
Toll Free 800 KLIM
TBA
rowan@velmoro-skyparts.com
www.velmoro.example
We will be moving to a new address with new numbers in the next few months, I would like to get the format prepared that will apply to multiple address' Card size European 9cm x 5.5cm

```html
<!DOCTYPE html>
<html lang="en">
<head>
<meta charset="utf-8">
<title>Velmoro Stationery</title>
<link rel="stylesheet" href="https://fonts.googleapis.com/css2?family=Open+Sans:wght@400;600;800&display=swap">
<style>
  :root {
    --backdrop: #ecebe8;
    --paper: #ffffff;
    --ink: #1d2a4a;
    --blue: #2185db;
    --blue-light: #55aef0;
    --grey: #6b6c6e;
    --grey-light: #9a9b9d;
    --caption: #55534f;
    --shadow: 0 2px 6px rgba(0,0,0,0.22);
  }
  * { box-sizing: border-box; margin: 0; padding: 0; }
  html, body { width: 1200px; height: 600px; overflow: hidden; }
  body {
    position: relative;
    background: var(--backdrop);
    font-family: "Open Sans", Arial, sans-serif;
    color: var(--ink);
  }
  .sheet { position: absolute; background: var(--paper); box-shadow: var(--shadow); overflow: hidden; }

  .brand { display: flex; align-items: center; gap: 6px; font-weight: 800; color: var(--ink); letter-spacing: 0.02em; white-space: nowrap; }
  .brand-dot { border-radius: 50%; background: var(--blue); flex: none; }

  /* business cards */
  .card { width: 163px; height: 100px; left: 24px; border-radius: 6px; }
  .card-front { top: 180px; }
  .card-back { top: 290px; }
  .card .brand { position: absolute; left: 12px; top: 14px; font-size: 11px; }
  .card .brand-dot { width: 12px; height: 12px; }
  .card-wave { position: absolute; left: 0; bottom: 0; width: 100%; }
  .card-details {
    position: absolute; left: 10px; right: 10px; bottom: 8px;
    display: flex; justify-content: space-between; color: var(--paper);
    font-size: 4.2px; line-height: 1.45;
  }
  .card-details .person-name { font-weight: 600; font-size: 5px; }

  /* letterhead */
  .letterhead { left: 221px; top: 29px; width: 396px; height: 540px; }
  .letterhead .brand { position: absolute; top: 24px; left: 50%; transform: translateX(-50%); font-size: 17px; }
  .letterhead .brand-dot { width: 18px; height: 18px; }
  .letterhead-band { position: absolute; left: 0; bottom: 0; width: 100%; height: 84px; }
  .letterhead-footer {
    position: absolute; left: 0; right: 0; bottom: 12px; text-align: center;
    color: var(--paper); font-size: 5px; line-height: 1.6;
  }

  /* envelopes */
  .envelope { left: 653px; width: 523px; }
  .envelope-flap { position: absolute; left: 0; top: 0; width: 100%; }
  .envelope-blue { top: 29px; height: 160px; }
  .envelope-grey { left: 684px; width: 468px; top: 180px; height: 150px; }
  .envelope-white { top: 283px; height: 137px; }
  .envelope-white .brand-dot { position: absolute; left: 50%; top: 20px; width: 22px; height: 22px; transform: translateX(-50%); }
  .envelope-front { top: 355px; width: 463px; height: 209px; }
  .envelope-front .brand { position: absolute; left: 22px; top: 22px; font-size: 14px; }
  .envelope-front .brand-dot { width: 15px; height: 15px; }
  .envelope-return { position: absolute; left: 22px; top: 54px; font-size: 4.5px; color: var(--grey); }

  .caption {
    position: absolute; top: 574px; font-size: 8px; letter-spacing: 0.12em;
    font-variant: small-caps; color: var(--caption);
  }
  .caption-letterhead { left: 358px; }
  .caption-envelope { left: 880px; }
</style>
</head>
<body>

  <!-- business card front -->
  <div class="sheet card card-front">
    <div class="brand"><span class="brand-dot"></span>VELMORO</div>
    <svg class="card-wave" viewBox="0 0 163 48" height="48" preserveAspectRatio="none">
      <defs>
        <linearGradient id="cardBlue" x1="0" x2="1"><stop offset="0" stop-color="#2185db"/><stop offset="1" stop-color="#55aef0"/></linearGradient>
      </defs>
      <path d="M0 14 Q80 34 163 6 L163 48 L0 48 Z" fill="url(#cardBlue)"/>
    </svg>
  </div>

  <!-- business card back -->
  <div class="sheet card card-back">
    <div class="brand"><span class="brand-dot"></span>VELMORO</div>
    <svg class="card-wave" viewBox="0 0 163 58" height="58" preserveAspectRatio="none">
      <path d="M0 10 Q80 28 163 4 L163 58 L0 58 Z" fill="url(#cardBlue)"/>
    </svg>
    <div class="card-details">
      <div>
        <div class="person-name">Rowan Pettibone</div>
        <div>Managing Director</div>
      </div>
      <div>
        <div>PO Box 71829 Marrow Bay Freezone</div>
        <div>Toll Free 800 KLIM</div>
        <div>rowan@velmoro-skyparts.com</div>
        <div>www.velmoro.example</div>
      </div>
    </div>
  </div>

  <!-- letterhead -->
  <div class="sheet letterhead">
    <div class="brand"><span class="brand-dot"></span>VELMORO</div>
    <svg class="letterhead-band" viewBox="0 0 396 84" preserveAspectRatio="none">
      <defs>
        <linearGradient id="letterBlue" x1="0" x2="1"><stop offset="0" stop-color="#2185db"/><stop offset="1" stop-color="#55aef0"/></linearGradient>
      </defs>
      <path d="M0 22 Q200 -6 396 18 L396 84 L0 84 Z" fill="#6b6c6e"/>
      <path d="M0 30 Q200 4 396 28 L396 84 L0 84 Z" fill="url(#letterBlue)"/>
    </svg>
    <div class="letterhead-footer">
      <div>PO Box 71829 Marrow Bay Freezone &nbsp;|&nbsp; Toll Free 800 KLIM</div>
      <div>rowan@velmoro-skyparts.com &nbsp;|&nbsp; www.velmoro.example</div>
    </div>
  </div>

  <!-- envelopes -->
  <div class="sheet envelope envelope-blue">
    <svg class="envelope-flap" viewBox="0 0 523 62" height="62" preserveAspectRatio="none">
      <path d="M0 0 H523 V30 Q262 70 0 30 Z" fill="url(#letterBlue)"/>
    </svg>
  </div>

  <div class="sheet envelope envelope-grey">
    <svg class="envelope-flap" viewBox="0 0 468 64" height="64" preserveAspectRatio="none">
      <path d="M0 0 H468 V34 Q234 70 0 34 Z" fill="#6b6c6e"/>
    </svg>
  </div>

  <div class="sheet envelope envelope-white">
    <svg class="envelope-flap" viewBox="0 0 523 60" height="60" preserveAspectRatio="none">
      <path d="M0 2 Q262 62 523 2" fill="none" stroke="#d6d6d6" stroke-width="1.2"/>
    </svg>
    <span class="brand-dot"></span>
  </div>

  <div class="sheet envelope envelope-front">
    <div class="brand"><span class="brand-dot"></span>VELMORO</div>
    <div class="envelope-return">PO Box 71829 Marrow Bay Freezone</div>
  </div>

  <div class="caption caption-letterhead">Letter-head Option 1</div>
  <div class="caption caption-envelope">Envelope Option 3</div>

</body>
</html>
```